Business Card Design

My business is writing crime novels to entertain readers. I write legal thrillers and mysteries. I need a card for publishers, agents, other authors, and media.

Industry/Entity Type

Legal

Contact Information for Business Card

Paul Ostrander
www.ostranderthrillers.example
paulbostrander@mailbox.example
0064 27 5139427

```html
<!DOCTYPE html>
<html lang="en">
<head>
<meta charset="utf-8">
<title>Paul Ostrander – Business Card</title>
<link rel="stylesheet" href="https://fonts.googleapis.com/css2?family=Gochi+Hand&family=Delius&display=swap">
<style>
  :root {
    --backdrop: #e9e4d8;
    --card-black: #050505;
    --card-edge-red: #e00000;
    --card-edge-red-dark: #7a0000;
    --card-edge-white: #ffffff;
    --accent-red: #e3121b;
    --text-light: #ececec;
    --portrait-grey: #9a9a9a;
    --portrait-dark: #4a4a4a;
    --pattern-red: rgba(120, 0, 0, 0.35);
  }
  * { box-sizing: border-box; margin: 0; padding: 0; }
  html, body {
    width: 1200px;
    height: 729px;
    overflow: hidden;
    background: var(--backdrop);
  }
  .canvas {
    position: relative;
    width: 1200px;
    height: 729px;
  }
  .business-card {
    position: absolute;
    left: 150px;
    top: 107px;
    width: 900px;
    height: 514px;
    border-radius: 30px;
    overflow: hidden;
    background: var(--card-black);
    box-shadow: 0 14px 30px rgba(0, 0, 0, 0.35);
  }
  .card-edge-top {
    position: absolute;
    left: 0; top: 0;
    width: 100%;
    height: 16px;
    background: linear-gradient(180deg, var(--card-edge-red) 0%, var(--card-edge-red-dark) 100%);
  }
  .card-edge-bottom {
    position: absolute;
    left: 0; bottom: 0;
    width: 100%;
    height: 18px;
    background: var(--card-edge-white);
  }
  .card-pattern {
    position: absolute;
    right: 0; top: 16px;
    width: 520px;
    height: 260px;
    background: radial-gradient(ellipse at 70% 20%, var(--pattern-red) 0%, rgba(0,0,0,0) 70%);
  }
  .portrait {
    position: absolute;
    left: 112px;
    top: 128px;
    width: 322px;
    height: 340px;
    border-radius: 26px;
    background: linear-gradient(180deg, var(--portrait-grey) 0%, #8a8a8a 60%, var(--portrait-dark) 100%);
    border: 2px solid #2a2a2a;
  }
  .author-name {
    position: absolute;
    left: 472px;
    top: 128px;
    font-family: "Gochi Hand", cursive;
    font-size: 60px;
    color: var(--accent-red);
    letter-spacing: 2px;
    line-height: 1;
  }
  .contact-list {
    position: absolute;
    left: 488px;
    top: 232px;
    list-style: none;
  }
  .contact-item {
    display: flex;
    align-items: center;
    gap: 14px;
    height: 40px;
    font-family: "Delius", sans-serif;
    font-size: 24px;
    color: var(--text-light);
  }
  .contact-icon {
    width: 20px;
    height: 20px;
    flex: none;
    fill: var(--accent-red);
  }
</style>
</head>
<body>
<main class="canvas">
  <article class="business-card">
    <div class="card-edge-top"></div>
    <div class="card-pattern" role="img" aria-label="Faint dark red swirl ornament"></div>
    <div class="portrait" role="img" aria-label="Author portrait photograph"></div>
    <h1 class="author-name">Paul Ostrander</h1>
    <ul class="contact-list">
      <li class="contact-item">
        <svg class="contact-icon" viewBox="0 0 20 20" aria-hidden="true">
          <path d="M2 6 Q10 1 18 6 L16 9 L13 8 L13 6.5 Q10 5.5 7 6.5 L7 8 L4 9 Z"/>
          <path d="M5 10 L15 10 L17 17 L3 17 Z"/>
        </svg>
        <span>0064 27 5139427</span>
      </li>
      <li class="contact-item">
        <svg class="contact-icon" viewBox="0 0 20 20" aria-hidden="true">
          <path d="M2 5 H18 V15 H2 Z M3.5 6.2 L10 11 L16.5 6.2 Z" fill-rule="evenodd"/>
        </svg>
        <span>paulbostrander@mailbox.example</span>
      </li>
      <li class="contact-item">
        <svg class="contact-icon" viewBox="0 0 20 20" aria-hidden="true">
          <circle cx="10" cy="10" r="8" fill="none" stroke="var(--accent-red)" stroke-width="1.8"/>
          <ellipse cx="10" cy="10" rx="3.5" ry="8" fill="none" stroke="var(--accent-red)" stroke-width="1.5"/>
          <path d="M2 10 H18 M3.5 6 H16.5 M3.5 14 H16.5" stroke="var(--accent-red)" stroke-width="1.5"/>
        </svg>
        <span>www.ostranderthrillers.example</span>
      </li>
    </ul>
    <div class="card-edge-bottom"></div>
  </article>
</main>
</body>
</html>
```